Wine Bottle Label

We would like a custom label for a wine bottle. We are a retailer of locally produced wines in a tourist town with a rich Dutch heritage. Our store is called The Vat Cellar (wijn is Dutch for wine). We would like something that says "Vat Cellar Red" and has a really classy look to it. We would also like to incorporate the "tulip bottle" in our logo which many customers recognize us by. Other traditional Dutch items like a windmill or a clog are optional. the design must incorporate the words "Pella, Iowa" somewhere as the tourist traffic always wants a "bottle that says Pella on it". Our customers are largely female and tend to be fans of the "buy local, drink local" crowd. We want something classic, but not pretentious. In my mind the background is dark or black, but will look at other options as well, will likely be on a black-glass bottle. If the color scheme could be changed very simply later to allow for a "Vat Cellar White" option that would be even better.

```html
<!DOCTYPE html>
<html lang="en">
<head>
<meta charset="utf-8">
<title>Vat Cellar Labels</title>
<link href="https://fonts.googleapis.com/css2?family=Montserrat:wght@400;500&display=swap" rel="stylesheet">
<style>
  :root {
    --canvas: #ffffff;
    --label-paper: #f4f4f4;
    --ink: #111111;
    --red-orange: #ff6a00;
    --red-purple: #6a2386;
    --red-crimson: #c4161c;
    --white-green: #85a92c;
    --white-yellow: #ffcc00;
    --white-blue: #1b5a78;
  }
  html, body {
    margin: 0;
    padding: 0;
    width: 1200px;
    height: 849px;
    overflow: hidden;
    background: var(--canvas);
  }
  .canvas {
    position: relative;
    width: 1200px;
    height: 849px;
    display: flex;
    flex-direction: column;
    align-items: center;
    justify-content: center;
    gap: 22px;
  }
  .label {
    position: relative;
    width: 447px;
    height: 387px;
    background: var(--label-paper);
    font-family: "Montserrat", sans-serif;
    color: var(--ink);
  }
  .label__townscape {
    position: absolute;
    left: 8px;
    top: 18px;
    width: 431px;
    height: 248px;
  }
  .label--red .label__townscape {
    background: linear-gradient(90deg,
      var(--red-orange) 0%, var(--red-orange) 13%,
      var(--red-purple) 14.5%, var(--red-purple) 27%,
      var(--red-crimson) 28.5%, var(--red-crimson) 42%,
      var(--red-orange) 43.5%, var(--red-orange) 57%,
      var(--red-purple) 58.5%, var(--red-purple) 71%,
      var(--red-orange) 72.5%, var(--red-orange) 85%,
      var(--red-crimson) 86.5%, var(--red-crimson) 100%);
  }
  .label--white .label__townscape {
    background: linear-gradient(90deg,
      var(--white-green) 0%, var(--white-green) 13%,
      var(--white-yellow) 14.5%, var(--white-yellow) 27%,
      var(--white-blue) 28.5%, var(--white-blue) 42%,
      var(--white-green) 43.5%, var(--white-green) 57%,
      var(--white-yellow) 58.5%, var(--white-yellow) 71%,
      var(--white-green) 72.5%, var(--white-green) 85%,
      var(--white-blue) 86.5%, var(--white-blue) 100%);
  }
  .label__title {
    position: absolute;
    left: 0;
    right: 0;
    top: 291px;
    margin: 0;
    text-align: center;
    font-weight: 400;
    font-size: 29px;
    letter-spacing: 2px;
    line-height: 1;
    text-transform: uppercase;
    white-space: nowrap;
  }
  .label__place {
    position: absolute;
    left: 0;
    right: 0;
    top: 328px;
    margin: 0;
    text-align: center;
    font-weight: 400;
    font-size: 22px;
    letter-spacing: 2.5px;
    line-height: 1;
    text-transform: uppercase;
    white-space: nowrap;
  }
</style>
</head>
<body>
  <main class="canvas">
    <section class="label label--red">
      <div class="label__townscape" role="img" aria-label="Row of tall Dutch canal houses in orange, purple and red with white windows, one leaning, a small bicycle at the base"></div>
      <h1 class="label__title">Vat Cellar Red</h1>
      <p class="label__place">Pella, Iowa</p>
    </section>
    <section class="label label--white">
      <div class="label__townscape" role="img" aria-label="Row of tall Dutch canal houses in green, yellow and blue with white windows, one leaning, a small bicycle at the base"></div>
      <h1 class="label__title">Vat Cellar White</h1>
      <p class="label__place">Pella, Iowa</p>
    </section>
  </main>
</body>
</html>
```